inspirational business card

I want to use the Vector on Pixmarra.com (number 61827405) and I will purchase the vector to send it to the designer once the general concept is approved. You can download it for free for a one time use on providing a design for this request.
Within the vector, insert:
Denise Halvorsen
Guidance and Cooperative

I prefer a vertical card but do not require vertical.

Contact info:

Denise Halvorsen, J.D.
Collaborative Lawyer
Certified Divorce Coach
Mediation Coach
PHONE 641/382-4076
EMAIL: dhrt@quelvo.net

Website: Guidanceandcooperative.com
Settlementcourse.com

I like greens, blue and grey. I do not want black font, and would like the font to be legible without needing perfect reading vision (no super small font).
I would like the overall theme to convey growth and nurturance.
I like the vector I selected because of the growth and light portrayed.
Not too frilly or too bold. I would like to to appeal to both sexes.

Target Market(s)

Generally professional women 35-60

Industry/Entity Type

Attorney

Font styles to use
Serif
Sans Serif

Colors
acd136
cadf82
fbf289
9d9d9d

Requirements
Must have
• My project does not need to have my photo but you could use it if you want
Nice to have
• Vertical
• I like rounded edges on the cards
Should not have
• I do not like my name appearing two times in close proximity. I'm not a flowery person.

```html
<!DOCTYPE html>
<html lang="en">
<head>
<meta charset="utf-8">
<title>Denise Halvorsen, J.D. — Business Card</title>
<link rel="stylesheet" href="https://fonts.googleapis.com/css2?family=Cinzel:wght@400;500&family=Questrial&display=swap">
<style>
  :root {
    --card-white: #ffffff;
    --band-green: #56b000;
    --rule-green: #7cc520;
    --label-green: #66b41c;
    --accent-green: #b9e05a;
    --name-grey: #56616a;
    --text-grey: #5d676d;
    --tree-light: #d9edc0;
    --tree-pale: #eef7e4;
    --photo-tone: #8b7f7a;
    --photo-dark: #3f4a55;
  }
  * { margin: 0; padding: 0; box-sizing: border-box; }
  html, body { width: 686px; height: 1200px; overflow: hidden; background: var(--card-white); }
  .card { position: relative; width: 686px; height: 1200px; overflow: hidden; background: var(--band-green); }
  .card-shape { position: absolute; inset: 0; }
  .tree-art {
    position: absolute; left: 0; top: 215px; width: 686px; height: 710px;
    background: radial-gradient(ellipse 52% 42% at 50% 40%, var(--tree-light) 0%, var(--tree-pale) 65%, rgba(255,255,255,0) 100%);
    opacity: 0.85;
  }
  .portrait {
    position: absolute; left: 194px; top: 114px; width: 298px; height: 298px; border-radius: 50%;
    background: radial-gradient(circle at 50% 45%, var(--photo-tone) 0%, var(--photo-dark) 100%);
  }
  .name {
    position: absolute; left: 0; right: 0; top: 470px; text-align: center;
    font-family: "Cinzel", serif; font-weight: 500; font-size: 50px; letter-spacing: 0.5px;
    color: var(--name-grey); line-height: 1;
  }
  .name-rule { position: absolute; left: 63px; top: 530px; width: 563px; height: 4px; background: var(--rule-green); }
  .titles {
    position: absolute; left: 0; right: 0; top: 544px; text-align: center;
    font-family: "Questrial", sans-serif; font-size: 38px; line-height: 48px; color: var(--text-grey);
  }
  .contact {
    position: absolute; left: 0; right: 0; top: 712px; text-align: center;
    font-family: "Questrial", sans-serif; font-size: 38px; line-height: 54px; color: var(--text-grey);
  }
  .contact .label { color: var(--label-green); }
  .website {
    position: absolute; left: 0; right: 0; top: 1054px; text-align: center;
    font-family: "Questrial", sans-serif; font-size: 39px; color: var(--card-white); letter-spacing: 0.3px;
  }
  .website .accent { color: var(--accent-green); }
</style>
</head>
<body>
  <div class="card">
    <svg class="card-shape" width="686" height="1200" viewBox="0 0 686 1200" aria-hidden="true">
      <path d="M0 0 H686 V835 C620 960 480 1008 343 1008 C206 1008 66 960 0 835 Z" fill="var(--card-white)"/>
    </svg>
    <div class="tree-art" role="img" aria-label="Faint pale green tree with leafy branches spreading behind the card text"></div>
    <div class="portrait" role="img" aria-label="Round portrait photograph of the attorney"></div>
    <h1 class="name">Denise Halvorsen, J.D.</h1>
    <div class="name-rule"></div>
    <p class="titles">Collaborative Lawyer<br>Certified Divorce Coach</p>
    <p class="contact">
      <span class="label">Ph:</span> 641.382.4076<br>
      <span class="label">email:</span> dhrt@quelvo.net
    </p>
    <p class="website">guidance<span class="accent">and</span>cooperative.com</p>
  </div>
</body>
</html>
```